Variso B2B Website
Website Design Project
Project: Variso B2B Website
Variso B2B Website - Software
Creative Brief
Software
will be www.varisosystems.example but currently is www.trendaware.example
Go to www.trendaware.example to either learn about company or see current site. We are changing our name to Variso Systems LLC with our logo as Variso. You can find our new logo in pixelorka. I have listed the green and blue color's used in our scheme below.
We have been a leader in France/Europe providing ATS (applicant tracking system) solutions in that market but now will be launching globally under Variso. We are a cloud based software that helps companies with their recruiting from helping to attract candidates to streamlining the recruiting workflow. Most likely, we will expand to provide additional cloud based talent solutions long term.
Variso is taken from the latin word meaning "shine". We chose Variso for a few reasons 1. shine describes what people do for their companies - they are the rays that reach out to their customer base, that create the competitive differential, that make a company succeed 2. Shine also depicts how our technology can help differentiate the company, market their opportunities, be the rays that reach out to relevant talent.
If you are not familiar with applicant tracking systems or cloud based software or SaaS just google the concepts.
Here is a cut from the site on Variso:
Variso provides easy to use talent management and applicant tracking software that gives you the power to hire top talent, reduce costs and continuously improve business performance. We designed our solution to maximize the experience of our four primary user groups: recruiters, hiring managers, executives and prospective candidates (both internal and external). Immediatly after implementation you will realize significant cost savings and efficiency gains while increasing your ability to attract, hire and retain the best talent.
With Trendaware’s talent management and applicant tracking software, your organization can :
•Drastically increase your recruiting effectiveness by automating your workflow from requisition to hire
•Boost your brand and relevant candidate flow through an engaging career site
•Increase your candidate pool quantity and quality through our comprehensive sourcing solution while ensuring OFCCP compliance
•Save time and money advertising your open positions on job boards, social networks, university career sites, etc. with one click using our award winning job board posting & analytics software
•Capture the most qualified applicants and gain recruiter efficiency through our resume parsing, searching and matching capabilities
•Automate your candidate screening through our flexible, customizable screening and scoring module
•Improve the ROI of your recruitment investments through our real time powerful reporting analytics
•Easily store and report EEO data and ensure compliance with OFCCP regulations
•Effectively communicate and engage with ideal candidates
Right now the logo has blues and greens. With Variso meaning shine yellow could be the third color, however grey, or other choices could be incorporated as well. I will leave that up to you.
The goal of the site is twofold: 1. to secure more requests for demo's and 2. to give prospects who have received information on us a way to gain more information. a thired goal would be to recruit talent and/or business partners. Our current site has the navigation below the fold which is difficult to see. in addition, the content is expanded horizontally through the use of multiple pages but it is hard to see that there is additional content. I would rather have the content vertically displayed. i like the site looking clean and modern , not overly cluttered. it needs to be able to appeal to multiple types of people therefore a place that lets them search by need is good.
High Tech
#CCFF00,#99CC00,#000000
#FFFFFF,#00CCFF,#0066FF
you choose as #1 & 2 color's are in our logo
www.hirobel.example - i like for clean, crisp feel
www.plumvoss.example - naviagation & presentation
www.keltiq.example - focus on demo & site

```html
<!DOCTYPE html>
<html lang="en">
<head>
<meta charset="utf-8">
<title>Variso — Talent Management Solutions</title>
<link href="https://fonts.googleapis.com/css2?family=Open+Sans:wght@400;600;700&family=Oswald:wght@300;400&display=swap" rel="stylesheet">
<style>
:root{
  --navy:#0b2f7a;
  --blue:#1656c9;
  --sky:#2f8fe8;
  --cyan:#00ccff;
  --lime:#ccff00;
  --green:#99cc00;
  --ink:#222;
  --muted:#666;
  --panel:#ffffff;
  --grey:#e4e6ea;
  --line:#c9ccd2;
}
*{box-sizing:border-box;margin:0;padding:0}
html,body{width:1200px;height:1072px;overflow:hidden}
body{font-family:"Open Sans",Arial,sans-serif;color:var(--ink);
  background:linear-gradient(180deg,#0e3d9e 0,#2a74d6 130px,#dfe8f5 300px,#f4f6f9 500px,#f4f6f9 100%);position:relative}
.site-header{position:absolute;left:160px;top:30px;width:920px;height:90px}
.brand{display:flex;align-items:center;gap:12px;position:absolute;left:0;top:8px}
.brand-mark{width:44px;height:44px;background:var(--green);border-radius:50%}
.brand-name{font-size:46px;font-weight:700;color:#fff;letter-spacing:1px}
.brand-tag{position:absolute;left:56px;top:62px;font-size:10px;color:#cfe0ff}
.top-tools{position:absolute;right:0;top:6px;display:flex;gap:6px}
.top-tools span{width:18px;height:18px;border-radius:3px;background:#fff;opacity:.85}
.top-tools .flag{width:22px;height:15px;margin-top:2px;border-radius:1px}
.main-nav{position:absolute;left:122px;top:128px;width:956px;height:46px;
  background:linear-gradient(180deg,#2a6fd8,#0e3f9f);border-radius:6px 6px 0 0;display:flex;align-items:center;padding:0 10px}
.main-nav a{color:#fff;text-decoration:none;font-size:14px;font-weight:600;padding:0 26px;height:46px;line-height:46px}
.main-nav a.active{background:linear-gradient(180deg,#eaffb0,#b6e22b);color:var(--navy);border-radius:6px 6px 0 0;margin-top:4px;height:42px;line-height:40px;padding:0 38px}
.main-nav .login{margin-left:auto;background:linear-gradient(180deg,#e3ff8a,#99cc00);color:var(--navy);border-radius:4px;height:32px;line-height:32px;padding:0 22px}
.hero{position:absolute;left:122px;top:174px;width:956px;height:310px;
  background:linear-gradient(180deg,#0d3a98 0,#1a58c4 60%,#2a7be0 100%)}
.hero h1{position:absolute;left:92px;top:46px;font-family:"Oswald",sans-serif;font-weight:300;font-size:42px;color:#fff;letter-spacing:1px}
.hero h2{position:absolute;left:92px;top:98px;width:400px;font-family:"Oswald",sans-serif;font-weight:300;font-size:29px;line-height:34px;color:var(--lime)}
.hero p{position:absolute;left:92px;top:172px;width:360px;font-size:11px;line-height:15px;color:#d8e6ff}
.demo-btn{position:absolute;left:92px;top:240px;width:156px;height:30px;border:1px solid #9cc3ff;border-radius:4px;
  background:linear-gradient(180deg,#4c90ee,#1c5bc9);color:#fff;font-family:"Oswald",sans-serif;font-size:15px;text-align:center;line-height:28px;letter-spacing:1px}
.player{position:absolute;left:472px;top:28px;width:444px;height:264px;background:var(--panel);border:3px solid #d7e3f6;border-radius:4px}
.player .screen{position:absolute;left:10px;top:10px;right:10px;bottom:34px;background:radial-gradient(circle at 50% 50%,#eaf4ff,#ffffff)}
.player .bar{position:absolute;left:10px;right:10px;bottom:8px;height:20px;background:#2b2f38;border-radius:2px}
.player .bar i{position:absolute;left:30px;top:9px;width:250px;height:3px;background:#6b7280}
.slide-arrow{position:absolute;top:312px;width:28px;height:28px;border-radius:50%;background:var(--green);color:#fff;font-size:16px;font-weight:700;text-align:center;line-height:27px}
.features{position:absolute;left:152px;top:488px;width:900px;height:58px;display:flex;gap:14px}
.feature{flex:1;background:linear-gradient(180deg,#ffffff,#e3ebf5);border:1px solid var(--line);border-radius:6px;position:relative;padding:10px 0 0 16px}
.feature b{display:block;font-size:17px;font-weight:600;color:var(--navy)}
.feature small{font-size:9px;color:var(--muted)}
.feature .ico{position:absolute;right:10px;top:9px;width:40px;height:38px;border-radius:4px;background:linear-gradient(180deg,#cfd6df,#8f99a6)}
.columns{position:absolute;left:152px;top:588px;width:900px;display:flex;gap:40px}
.col{flex:1}
.col h3{font-size:29px;font-weight:700;color:#333;line-height:34px;margin-bottom:12px}
.col h3 em{font-style:normal;color:var(--blue)}
.col p,.col li{font-size:10px;line-height:13.5px;color:#444}
.col ul{list-style:none;margin:10px 0}
.col .more{display:flex;align-items:center;gap:5px;margin-top:12px;font-size:10px;font-weight:600;color:var(--blue)}
.col .more:before{content:"";width:9px;height:9px;border-radius:50%;background:var(--blue)}
.news-item{margin-bottom:12px}
.news-item .date{color:var(--blue);font-size:10px;font-weight:600}
.news-item a{color:var(--blue)}
.why{position:absolute;left:140px;top:862px;width:920px;height:92px;border-radius:10px;
  background:linear-gradient(180deg,#f2f3f5,#c6cad1);border:1px solid #b3b8c0;display:flex;align-items:center}
.why-label{width:186px;padding-left:24px;font-size:24px;font-weight:600;color:#555;white-space:nowrap}
.why-list{flex:1;display:flex;justify-content:space-around;padding-right:8px}
.why-item{width:112px;text-align:center;font-size:10px;line-height:12px;color:var(--navy);font-weight:600}
.why-item svg{display:block;margin:0 auto 6px}
.site-footer{position:absolute;left:0;top:984px;width:1200px;height:88px;background:linear-gradient(180deg,#1f63cf,#0c3690)}
.footer-nav{position:absolute;left:148px;top:14px;display:flex;gap:56px}
.footer-nav a{color:#fff;font-size:10px;text-decoration:none}
.copyright{position:absolute;left:148px;top:32px;font-size:9px;color:#cfe0ff}
</style>
</head>
<body>
<header class="site-header">
  <div class="brand"><span class="brand-mark"></span><span class="brand-name">Variso</span></div>
  <div class="brand-tag">talent management solutions designed for you</div>
  <div class="top-tools">
    <span></span><span></span><span></span>
    <span class="flag" style="background:linear-gradient(90deg,#1f3c9e 33%,#fff 33% 66%,#d22 66%)"></span>
    <span class="flag" style="background:linear-gradient(90deg,#2a9d3b 33%,#fff 33% 66%,#d22 66%)"></span>
    <span class="flag" style="background:linear-gradient(180deg,#000 33%,#d22 33% 66%,#fc0 66%)"></span>
    <span class="flag" style="background:linear-gradient(180deg,#c22 0 20%,#fff 20% 40%,#c22 40% 60%,#fff 60% 80%,#1f3c9e 80%)"></span>
  </div>
</header>

<nav class="main-nav">
  <a class="active">Home</a><a>About Us</a><a>Our Solution</a><a>Partners</a><a>Customers</a><a>Resources</a>
  <a class="login">Customer Login</a>
</nav>

<section class="hero">
  <h1>WELCOME TO VARISO</h1>
  <h2>TALENT MANAGEMENT SOLUTIONS DESIGNED FOR YOU</h2>
  <p>Variso provides easy to use talent management and applicant tracking software that gives you the power to hire top talent, reduce costs and continuously improve business performance.</p>
  <div class="demo-btn">REQUEST A DEMO</div>
  <div class="player">
    <div class="screen" role="img" aria-label="Product introduction video frame"></div>
    <div class="bar"><i></i></div>
  </div>
</section>
<div class="slide-arrow" style="left:110px">‹</div>
<div class="slide-arrow" style="left:1062px">›</div>

<section class="features">
  <div class="feature"><b>Watch Video</b><small>See what we do</small><span class="ico" role="img" aria-label="Video camera icon"></span></div>
  <div class="feature"><b>Request Demo</b><small>See how we can help you</small><span class="ico" role="img" aria-label="Monitor icon"></span></div>
  <div class="feature"><b>Variso Version 3</b><small>All the tools you need</small><span class="ico" role="img" aria-label="Disc icon"></span></div>
  <div class="feature"><b>Testimonials</b><small>Hear from happy clients</small><span class="ico" role="img" aria-label="Person silhouette icon"></span></div>
</section>

<section class="columns">
  <div class="col">
    <h3>Who is <em>Variso?</em></h3>
    <p>Variso provides easy to use talent management and applicant tracking software that gives you the power to hire top talent, reduce costs and continuously improve business performance. We designed our solution to maximize the experience of our four primary user groups: recruiters, hiring managers, executives and prospective candidates (both internal and external). Immediatly after implementation you will realize significant cost savings and efficiency gains while increasing your ability to attract, hire and retain the best talent.</p>
    <div class="more">Learn More</div>
  </div>
  <div class="col">
    <h3>Become a <em>Partner</em></h3>
    <p>We currently operate in several countries and are continuing to expand globally. We're currently looking for:</p>
    <ul><li>• Business Development Partners</li><li>• Application Partners</li><li>• Recruitment Process &amp; Integration Consultants</li></ul>
    <p>Contact us today to begin exploring what we can offer each other.</p>
    <div class="more">Learn More</div>
  </div>
  <div class="col">
    <h3>Latest <em>News</em></h3>
    <div class="news-item"><div class="date">May 12, 2011</div><p>Variso launches its recruiting platform worldwide with new career site tools for growing teams. <a>more</a></p></div>
    <div class="news-item"><div class="date">June 3, 2011</div><p>New reporting analytics module now helps clients measure hiring results in real time. <a>more</a></p></div>
    <div class="more">More News</div>
  </div>
</section>

<section class="why">
  <div class="why-label">Why Variso?</div>
  <div class="why-list">
    <div class="why-item"><svg width="34" height="30"><ellipse cx="17" cy="15" rx="16" ry="10" fill="#1656c9"/><circle cx="17" cy="15" r="5" fill="#fff"/></svg>R&amp;D<br>Focused</div>
    <div class="why-item"><svg width="34" height="30"><circle cx="17" cy="16" r="12" fill="none" stroke="#1656c9" stroke-width="4"/><path d="M17 16V9" stroke="#1656c9" stroke-width="3"/></svg>Fast &amp; Easy<br>Implementation</div>
    <div class="why-item"><svg width="34" height="30"><circle cx="14" cy="16" r="10" fill="#1656c9"/><circle cx="14" cy="16" r="4" fill="#fff"/><circle cx="27" cy="8" r="6" fill="#1656c9"/></svg>Highly<br>Configurable</div>
    <div class="why-item"><svg width="34" height="30"><path d="M8 3h18v8a9 9 0 0 1-18 0z" fill="#1656c9"/><rect x="14" y="20" width="6" height="5" fill="#1656c9"/><rect x="9" y="25" width="16" height="4" fill="#1656c9"/></svg>Committed to<br>Your Success</div>
    <div class="why-item"><svg width="34" height="30"><rect x="4" y="3" width="26" height="18" rx="2" fill="#99cc00"/><rect x="14" y="21" width="6" height="5" fill="#1656c9"/><rect x="8" y="26" width="18" height="3" fill="#1656c9"/></svg>Cutting Edge<br>SaaS Technology</div>
    <div class="why-item"><svg width="34" height="30"><circle cx="10" cy="8" r="5" fill="#1656c9"/><circle cx="24" cy="8" r="5" fill="#1656c9"/><rect x="4" y="15" width="12" height="14" rx="4" fill="#1656c9"/><rect x="18" y="15" width="12" height="14" rx="4" fill="#1656c9"/></svg>Financially<br>Strong</div>
  </div>
</section>

<footer class="site-footer">
  <nav class="footer-nav"><a>Home</a><a>About Us</a><a>Our Solution</a><a>Partners</a><a>Customers</a><a>Resources</a></nav>
  <div class="copyright">All Rights Reserved © 2011 Variso, Inc.</div>
</footer>
</body>
</html>
```